Kestrel FM
Stationary and Business card Design
Simple
Adaeze T. Ibekwe
Managing Director
14 Umuola Lane, Ekwe Ridge, Aba. Nigeria, West Africa.
atibekwe@kestrelfmx.com
www.kestrelfmx.com
There are place holders, so keep each layer separated, and put each item (e.g. telephone number, name,etc) on separate levels to allow easy editing in both ai and psd files.
Infinity logo sign

```html
<!DOCTYPE html>
<html lang="en">
<head>
<meta charset="utf-8">
<title>Kestrel FM – Stationery</title>
<link rel="stylesheet" href="https://fonts.googleapis.com/css2?family=Questrial&display=swap">
<style>
  :root {
    --red: #e8262d;
    --black: #1a1a1a;
    --grey: #6b6b6b;
    --pale: #d9d9d9;
    --paper: #ffffff;
    --frame: #333333;
  }
  * { box-sizing: border-box; margin: 0; padding: 0; }
  html, body { width: 1200px; height: 701px; overflow: hidden; background: var(--paper); }
  body { position: relative; font-family: "Questrial", "Century Gothic", sans-serif; color: var(--black); }
  .piece { position: absolute; background: var(--paper); border: 1px solid var(--frame); overflow: hidden; }
  .abs { position: absolute; }

  .wordmark { position: absolute; display: flex; align-items: center; gap: 10px; white-space: nowrap; color: var(--black); letter-spacing: 0.5px; }
  .wordmark .dot { border-radius: 50%; background: var(--red); flex: none; }

  /* Business card front */
  .card-front { left: 105px; top: 83px; width: 338px; height: 192px; }
  .card-front .contact-column { left: 0; top: 0; width: 90px; height: 100%; background: var(--red); padding: 6px 5px; display: flex; flex-direction: column; justify-content: space-between; }
  .contact-item { background: rgba(255,255,255,0.18); color: #fff; text-align: center; font-size: 6.5px; line-height: 1.25; padding: 4px 2px; min-height: 38px; display: flex; flex-direction: column; align-items: center; justify-content: center; gap: 2px; }
  .contact-item svg { width: 13px; height: 13px; fill: var(--black); }
  .card-front .wordmark { left: 122px; top: 12px; font-size: 34px; }
  .card-front .wordmark .dot { width: 24px; height: 24px; }
  .card-front .person-name { left: 140px; top: 64px; font-size: 21px; }
  .card-front .person-title { right: 28px; top: 92px; font-size: 11px; color: var(--grey); }

  /* Business card back */
  .card-back { left: 100px; top: 370px; width: 345px; height: 200px; }
  .card-back .wordmark { left: 50%; top: 50%; transform: translate(-50%, -50%); font-size: 44px; }
  .card-back .wordmark .dot { width: 30px; height: 30px; }

  .rule-black { position: absolute; height: 3px; background: var(--black); }
  .band-red { position: absolute; background: var(--red); }

  /* Letterhead */
  .letterhead { left: 600px; top: 38px; width: 550px; height: 654px; }
  .letterhead .wordmark { left: 10px; top: 34px; font-size: 48px; }
  .letterhead .wordmark .dot { width: 34px; height: 34px; }
  .letterhead .person-name { left: 338px; top: 48px; font-size: 25px; }
  .letterhead .person-title { left: 366px; top: 78px; font-size: 14px; color: var(--grey); }
  .letterhead .watermark { left: 50%; top: 362px; transform: translate(-50%, -50%); font-size: 58px; color: var(--pale); }
  .letterhead .watermark .dot { width: 44px; height: 44px; background: #f6c9cb; }

  .letter-footer { left: 5px; right: 5px; top: 580px; height: 60px; display: flex; }
  .footer-item { flex: 1; display: flex; flex-direction: column; align-items: center; justify-content: space-between; font-size: 11.5px; text-align: center; line-height: 1.15; padding: 0 4px; }
  .footer-item + .footer-item { border-left: 2px solid var(--red); }
  .footer-item svg { width: 18px; height: 18px; fill: var(--black); }
  .footer-item.address { flex: 1.05; font-size: 10px; }
  .footer-item.email { flex: 1.1; }
  .footer-item.phone { flex: 0.65; }
</style>
</head>
<body>

<svg width="0" height="0" style="position:absolute">
  <defs>
    <symbol id="icon-home" viewBox="0 0 24 24"><path d="M12 2 1 12h3v10h6v-6h4v6h6V12h3z"/></symbol>
    <symbol id="icon-mail" viewBox="0 0 24 24"><path d="M2 5h20v14H2z M3 6l9 7 9-7" fill-rule="evenodd"/><path d="M3.5 6.5 12 13l8.5-6.5" fill="none" stroke="#fff" stroke-width="1.6"/></symbol>
    <symbol id="icon-phone" viewBox="0 0 24 24"><path d="M6.6 10.8a15 15 0 0 0 6.6 6.6l2.2-2.2a1 1 0 0 1 1-.25 11.4 11.4 0 0 0 3.6.57 1 1 0 0 1 1 1V20a1 1 0 0 1-1 1A17 17 0 0 1 3 4a1 1 0 0 1 1-1h3.5a1 1 0 0 1 1 1c0 1.25.2 2.45.57 3.6a1 1 0 0 1-.25 1z"/></symbol>
    <symbol id="icon-web" viewBox="0 0 24 24"><circle cx="12" cy="12" r="11"/><path d="M12 6v12M6 12h12" stroke="#fff" stroke-width="2.4"/></symbol>
  </defs>
</svg>

<!-- Business card front -->
<section class="piece card-front" aria-label="Business card front">
  <div class="abs contact-column">
    <div class="contact-item"><svg><use href="#icon-home"/></svg><span class="address">14 Umuola Lane,<br>Ekwe Ridge, Aba.<br>Nigeria, West Africa.</span></div>
    <div class="contact-item"><svg><use href="#icon-mail"/></svg><span class="email">atibekwe@kestrelfmx.com</span></div>
    <div class="contact-item"><svg><use href="#icon-phone"/></svg><span class="phone">555-555-5555</span></div>
    <div class="contact-item"><svg><use href="#icon-web"/></svg><span class="website">www.kestrelfmx.com</span></div>
  </div>
  <div class="wordmark"><span>Kestrel FM</span><span class="dot"></span></div>
  <p class="abs person-name">Adaeze T. Ibekwe</p>
  <p class="abs person-title">Managing Director</p>
</section>

<!-- Business card back -->
<section class="piece card-back" aria-label="Business card back">
  <div class="rule-black" style="left:0;right:0;top:8px"></div>
  <div class="band-red" style="left:60px;right:0;top:16px;height:10px"></div>
  <div class="wordmark"><span>Kestrel FM</span><span class="dot"></span></div>
  <div class="band-red" style="left:0;width:275px;top:168px;height:10px"></div>
  <div class="rule-black" style="left:0;right:0;top:185px"></div>
</section>

<!-- Letterhead -->
<section class="piece letterhead" aria-label="Letterhead">
  <div class="rule-black" style="left:5px;right:5px;top:7px"></div>
  <div class="band-red" style="left:188px;right:5px;top:17px;height:13px"></div>
  <div class="wordmark"><span>Kestrel FM</span><span class="dot"></span></div>
  <p class="abs person-name">Adaeze T. Ibekwe</p>
  <p class="abs person-title">Managing Director</p>
  <div class="wordmark watermark" aria-hidden="true"><span>Kestrel FM</span><span class="dot"></span></div>
  <footer class="abs letter-footer">
    <div class="footer-item address"><svg><use href="#icon-home"/></svg><span>14 Umuola Lane,<br>Ekwe Ridge, Aba.<br>Nigeria, West Africa.</span></div>
    <div class="footer-item email"><svg><use href="#icon-mail"/></svg><span>atibekwe@kestrelfmx.com</span></div>
    <div class="footer-item phone"><svg><use href="#icon-phone"/></svg><span>555-555-5555</span></div>
    <div class="footer-item website"><svg><use href="#icon-web"/></svg><span>www.kestrelfmx.com</span></div>
  </footer>
</section>

</body>
</html>
```